We (R. T. Halvering & Associates, Inc.) are an executive Search firm based in Los Angeles that is exclusively focused in the Med Tech and Health Tech arenas.   I need a logo to communicate that we are a high end search firm, but also that we are focused in the medicine and science arenas called health tech and med tech.  Many of our clients have robotics and artificial intelligence type products, so it is very technology forward.  I tend to gravitate towards clean, sharp aesthetic as opposed to something that is really over the top.
Attached are files with my logo in two different layouts.  In addition to the letterhead and envelope, I also will need an electronic letterhead in Microsoft Word.  I tend to
I look forward to seeing the designs and just let me know if you have any questions.
Dale

```html
<!DOCTYPE html>
<html lang="en">
<head>
<meta charset="utf-8">
<title>R. T. Halvering &amp; Associates, Inc. — Stationery</title>
<link href="https://fonts.googleapis.com/css2?family=Montserrat:wght@300;400;500;600&family=Arimo:wght@400&display=swap" rel="stylesheet">
<style>
:root{
  --board:#a9a9a9;
  --paper:#ffffff;
  --paper-shade:#e4e4e6;
  --brand-blue:#52a3da;
  --ink:#1b1b1b;
  --muted:#9b9b9b;
  --rule:#3a3a3a;
  --shadow:rgba(0,0,0,.35);
}
*{margin:0;padding:0;box-sizing:border-box}
html,body{width:1200px;height:1190px;overflow:hidden}
body{background:var(--board);position:relative;font-family:"Montserrat",sans-serif;color:var(--ink)}
.piece{position:absolute;box-shadow:2px 2px 3px var(--shadow);overflow:hidden}

/* wordmark */
.wordmark{position:absolute;display:flex;align-items:center;gap:12px}
.wordmark .dot{border-radius:50%;background:var(--brand-blue);flex:none}
.wordmark .name{font-family:"Montserrat",sans-serif;font-weight:500;color:var(--ink);line-height:1}
.wordmark .name .firm{display:block;letter-spacing:-.3px}
.wordmark .name .assoc{display:block;letter-spacing:2.4px;margin-top:3px}

.contact{position:absolute;font-family:"Arimo",sans-serif;color:var(--ink)}
.contact p{display:flex;align-items:center;gap:4px;white-space:nowrap}
.contact svg{fill:var(--brand-blue);flex:none}

/* letterhead */
.letterhead{left:40px;top:50px;width:555px;height:785px;background:linear-gradient(100deg,#f1f1f2 0%,#fbfbfb 60%,#fff 100%)}
.letterhead .wordmark{left:37px;top:38px}
.letterhead .dot{width:20px;height:20px}
.letterhead .firm{font-size:21px}
.letterhead .assoc{font-size:9px}
.letterhead .contact{left:421px;top:30px;font-size:8.8px;line-height:10.4px}
.letterhead .contact .gap{margin-bottom:4px}
.letterhead .rule{position:absolute;left:37px;top:91px;width:481px;height:1px;background:var(--rule)}
.recipient{position:absolute;left:57px;top:175px;font-size:7.4px;color:var(--muted);line-height:12px}
.recipient .to{font-size:10px;color:var(--ink);letter-spacing:1.5px;margin-bottom:3px}
.recipient .who{font-size:9px;color:var(--brand-blue);font-weight:500;margin-bottom:2px}
.date{position:absolute;right:56px;top:175px;font-size:7.6px;color:var(--muted)}
.body-copy{position:absolute;left:57px;top:281px;width:444px;font-size:8.3px;font-weight:300;color:#8a8a8a;line-height:9.9px;text-align:justify}
.body-copy p{margin-bottom:9.8px}
.signature{position:absolute;left:57px;top:553px;width:96px;height:22px;background:#e3e3e3;border-radius:3px}
.signer{position:absolute;left:57px;top:584px;font-size:9px;font-weight:500;line-height:12px}
.signer span{display:block;font-size:7.4px;font-weight:300;color:var(--muted)}

/* folder cover */
.folder-cover{left:622px;top:50px;width:538px;height:380px;background:linear-gradient(90deg,#d3d3d5 50%,#eeeeef 62%,#fff 80%)}
.folder-cover .spine-panel{position:absolute;left:0;top:0;width:269px;height:100%;background:var(--brand-blue)}
.folder-cover .wordmark{left:328px;top:173px;gap:10px}
.folder-cover .dot{width:16px;height:16px}
.folder-cover .firm{font-size:16.5px}
.folder-cover .assoc{font-size:6.8px;letter-spacing:1.8px;margin-top:2px}
.folder-cover .contact{left:364px;top:357px;font-size:3.6px;line-height:4.4px;display:flex;gap:4px}
.folder-cover .contact .left{text-align:right;padding-right:4px;border-right:.5px solid #555}

/* open folder */
.folder-open{left:624px;top:458px;width:534px;height:377px;background:linear-gradient(90deg,#fff 0%,#f1f1f2 30%,#e0e0e2 50%,#c9c9cb 50%,#dcdcde 56%,#f4f4f5 100%)}
.folder-open .pockets{position:absolute;left:0;top:0}
.mini-letter{position:absolute;left:280px;top:18px;width:242px;height:226px;background:linear-gradient(100deg,#efeff0,#fff);box-shadow:0 0 2px rgba(0,0,0,.2)}
.mini-letter .wordmark{left:17px;top:17px;gap:6px}
.mini-letter .dot{width:9px;height:9px}
.mini-letter .firm{font-size:9px}
.mini-letter .assoc{font-size:3.8px;letter-spacing:1px;margin-top:1px}
.mini-letter .contact{left:183px;top:13px;font-size:3.4px;line-height:4px}
.mini-letter .rule{position:absolute;left:16px;top:40px;width:210px;height:.5px;background:var(--rule)}
.mini-letter .recipient{left:25px;top:76px;font-size:3.2px;line-height:5.2px}
.mini-letter .recipient .to{font-size:4.4px;margin-bottom:1px;letter-spacing:.6px}
.mini-letter .recipient .who{font-size:3.9px;margin-bottom:0}
.mini-letter .date{right:24px;top:76px;font-size:3.3px}
.mini-letter .body-copy{left:25px;top:122px;width:192px;font-size:3.6px;line-height:4.3px}
.mini-letter .body-copy p{margin-bottom:4px}

/* envelope front */
.envelope-front{left:40px;top:864px;width:548px;height:238px;background:linear-gradient(100deg,#ececed 0%,#f8f8f8 45%,#fff 100%)}
.envelope-front .wordmark{left:20px;top:22px;gap:10px}
.envelope-front .dot{width:16px;height:16px}
.envelope-front .firm{font-size:16px}
.envelope-front .assoc{font-size:6.6px;letter-spacing:1.9px;margin-top:2px}
.envelope-front .return{position:absolute;left:60px;top:55px;font-family:"Arimo",sans-serif;font-size:8.6px;line-height:10px}

/* envelope back */
.envelope-back{left:625px;top:870px;width:527px;height:228px;background:linear-gradient(90deg,#f4f4f5,#fff 60%)}
.envelope-back svg{position:absolute;left:0;top:0}
.envelope-back .wordmark{left:210px;top:18px;gap:10px}
.envelope-back .dot{width:16px;height:16px}
.envelope-back .firm{font-size:16px}
.envelope-back .assoc{font-size:6.6px;letter-spacing:1.9px;margin-top:2px}
</style>
</head>
<body>

<!-- Letterhead -->
<section class="piece letterhead" aria-label="Letterhead">
  <div class="wordmark"><span class="dot"></span><span class="name"><span class="firm">R. T. HALVERING</span><span class="assoc">&amp; ASSOCIATES INC.</span></span></div>
  <div class="contact">
    <p>Your address, city</p>
    <p class="gap">state, ZIP 0000</p>
    <p><svg width="7" height="7" viewBox="0 0 10 10"><path d="M2 0l2 2.5-1 1.3c.7 1.4 1.8 2.5 3.2 3.2l1.3-1L10 8l-1.5 2C4 9.6.4 6 0 1.5z"/></svg>555-014-2100</p>
    <p><svg width="7" height="6" viewBox="0 0 10 8"><path d="M0 0h10v8H0z M1 1l4 3 4-3" fill-rule="evenodd"/></svg>office@rthalvering.com</p>
    <p><svg width="7" height="7" viewBox="0 0 10 10"><circle cx="5" cy="5" r="5"/><path d="M0 5h10M5 0c-2 3-2 7 0 10M5 0c2 3 2 7 0 10" stroke="#fff" stroke-width=".8" fill="none"/></svg>www.rthalvering.com</p>
  </div>
  <div class="rule"></div>

  <div class="recipient">
    <div class="to">TO</div>
    <div class="who">Dana Whitlock</div>
    <div>Human Resources</div>
    <div>Corvane Labs</div>
    <div>48 Alder Row, Pasadena</div>
    <div>CA 91101 USA</div>
  </div>
  <div class="date">Friday, 01/01/2018</div>

  <div class="body-copy">
    <p>Lorem ipsum dolor sit amet, consectetuer adipiscing elit, sed diam nonummy nibh euismod tincidunt ut laoreet dolore magna aliquam erat volutpat. Ut wisi enim ad minim veniam, quis nostrud exerci tation ullamcorper suscipit lobortis nisl ut aliquip ex ea commodo consequat. Duis autem vel eum iriure dolor in hendrerit in vulputate velit esse molestie consequat, vel illum dolore eu feugiat nulla facilisis at vero eros et accumsan et iusto odio dignissim qui blandit praesent luptatum zzril delenit augue duis dolore te feugait nulla facilisi.</p>
    <p>Nam liber tempor cum soluta nobis eleifend option congue nihil imperdiet doming id quod mazim placerat facer possim assum. Typi non habent claritatem insitam;</p>
    <p>Est usus legentis in iis qui facit eorum claritatem.</p>
    <p>Investigationes demonstraverunt lectores legere me lius quod ii legunt saepius. Claritas est etiam processus dynamicus, qui sequitur mutationem consuetudium lectorum. Mirum est notare quam littera gothica, quam nunc putamus parum claram, anteposuerit litterarum formas humanitatis per seacula quarta decima et quinta decima. Eodem modo typi, qui nunc nobis videntur parum clari, fiant sollemnes in futurum.</p>
    <p>consectetuer adipiscing elit, sed diam nonummy nibh euismod tincidunt ut laoreet dolore magna aliquam erat volutpat. Ut wisi enim ad minim veniam, quis nostrud exerci tation ullamcorper suscipit lobortis nisl ut aliquip ex ea commodo consequat. Duis autem vel eum iriure dolor in hendrerit in vulputate velit esse molestie consequat, vel illum dolore eu feugiat nulla facilisis at vero eros et accumsan et iusto odio dignissim qui blandit praesent luptatum zzril delenit augue duis dolore te feugait nulla facilisi.</p>
    <p>Nam liber tempor cum soluta nobis eleifend option congue nihil imperdiet .</p>
  </div>

  <div class="signature" role="img" aria-label="Handwritten signature of Evan Marsh"></div>
  <div class="signer">Evan Marsh<span>Managing Director</span></div>
</section>

<!-- Folder cover -->
<section class="piece folder-cover" aria-label="Presentation folder, outside">
  <div class="spine-panel"></div>
  <div class="wordmark"><span class="dot"></span><span class="name"><span class="firm">R. T. HALVERING</span><span class="assoc">&amp; ASSOCIATES INC.</span></span></div>
  <div class="contact">
    <div class="left"><div>Your address, city</div><div>state, ZIP 0000</div></div>
    <div><div>555-014-2100</div><div>office@rthalvering.com</div><div>www.rthalvering.com</div></div>
  </div>
</section>

<!-- Folder inside -->
<section class="piece folder-open" aria-label="Presentation folder, inside">
  <div class="mini-letter">
    <div class="wordmark"><span class="dot"></span><span class="name"><span class="firm">R. T. HALVERING</span><span class="assoc">&amp; ASSOCIATES INC.</span></span></div>
    <div class="contact">
      <p>Your address, city</p>
      <p>state, ZIP 0000</p>
      <p>555-014-2100</p>
      <p>office@rthalvering.com</p>
      <p>www.rthalvering.com</p>
    </div>
    <div class="rule"></div>
    <div class="recipient">
      <div class="to">TO</div>
      <div class="who">Dana Whitlock</div>
      <div>Human Resources</div>
      <div>Corvane Labs</div>
      <div>48 Alder Row, Pasadena</div>
      <div>CA 91101 USA</div>
    </div>
    <div class="date">Friday, 01/01/2018</div>
    <div class="body-copy">
      <p>We are pleased to share our proposal for your upcoming leadership search in medical technology. Our team will guide every step with care and clear updates.</p>
      <p>Please review the attached terms at your convenience.</p>
      <p>Our process begins with a detailed discovery call, followed by market mapping, candidate outreach and structured interviews with your hiring team.</p>
      <p>We welcome your questions and look forward to speaking soon.</p>
    </div>
  </div>
  <svg class="pockets" width="534" height="377" viewBox="0 0 534 377" aria-hidden="true">
    <path d="M0 244H240Q252 244 253 257L267 377H0Z" fill="var(--brand-blue)"/>
    <path d="M267 377L283 259Q285 244 300 244H534V377Z" fill="var(--brand-blue)"/>
  </svg>
</section>

<!-- Envelope front -->
<section class="piece envelope-front" aria-label="Envelope, front">
  <div class="wordmark"><span class="dot"></span><span class="name"><span class="firm">R. T. HALVERING</span><span class="assoc">&amp; ASSOCIATES INC.</span></span></div>
  <div class="return">Your address, city<br>state, ZIP 0000</div>
</section>

<!-- Envelope back -->
<section class="piece envelope-back" aria-label="Envelope, back">
  <svg width="527" height="228" viewBox="0 0 527 228" aria-hidden="true">
    <defs>
      <filter id="flap-shadow" x="-5%" y="-20%" width="110%" height="160%"><feDropShadow dx="0" dy="3" stdDeviation="3" flood-color="#000" flood-opacity=".18"/></filter>
    </defs>
    <path d="M0 0H527L512 40Q504 62 480 62H47Q23 62 15 40Z" fill="#fff" filter="url(#flap-shadow)"/>
  </svg>
  <div class="wordmark"><span class="dot"></span><span class="name"><span class="firm">R. T. HALVERING</span><span class="assoc">&amp; ASSOCIATES INC.</span></span></div>
</section>

</body>
</html>
```